Yard Sign Design Needed

Yard sign needed for mowing & landscaping company. Would like to use the top logo with black background which is attached. Would like MOWING to be in large standout letters. The word "landscaping" can be smaller and more artistic or omitted. Will need room for phone number once design is approved. The phone number will need to stand out and look identical/similar to the word 'MOWING"

```html
<!DOCTYPE html>
<html lang="en">
<head>
<meta charset="utf-8">
<title>Brixton Contractors Yard Signs</title>
<link rel="stylesheet" href="https://fonts.googleapis.com/css2?family=Montserrat:wght@700;900&family=Cinzel:wght@700&display=swap">
<style>
  :root {
    --black: #060808;
    --logo-black: #040707;
    --grey: #e6e7e9;
    --green: #a6cf45;
    --white: #ffffff;
    --ink: #070707;
  }
  * { margin: 0; padding: 0; box-sizing: border-box; }
  html, body { width: 1200px; height: 555px; overflow: hidden; background: var(--white); }
  .canvas { position: relative; width: 1200px; height: 555px; }

  .sign { position: absolute; }
  .panel { position: absolute; }
  .panel--black { background: var(--black); }
  .panel--grey { background: var(--grey); }
  .panel--green { background: var(--green); }

  .brand-block {
    position: absolute;
    background: var(--logo-black);
    display: flex; flex-direction: column; align-items: center; justify-content: center;
    color: var(--green);
    font-family: "Montserrat", sans-serif; font-weight: 700;
    text-align: center; line-height: 1.15;
  }
  .brand-mark { background: var(--green); margin-bottom: 18px; }
  .brand-name { letter-spacing: 0.04em; }

  .headline {
    position: absolute;
    display: flex; flex-direction: column; align-items: stretch;
  }
  .headline__main {
    font-family: "Montserrat", sans-serif; font-weight: 900;
    color: var(--ink); text-align: center; line-height: 1; letter-spacing: -0.01em;
  }
  .headline__sub {
    background: var(--ink); color: var(--white);
    font-family: "Cinzel", serif; font-weight: 700;
    text-align: center; line-height: 1;
    display: flex; align-items: center; justify-content: center;
  }

  .phone {
    position: absolute;
    display: flex; align-items: center;
    font-family: "Montserrat", sans-serif; font-weight: 900; color: var(--ink);
    line-height: 1;
  }
  .phone__icon { flex: none; display: block; }

  /* Portrait sign */
  .sign--portrait { left: 0; top: 0; width: 416px; height: 555px; }
  .sign--portrait .panel--black { left: 0; top: 0; width: 416px; height: 278px; }
  .sign--portrait .panel--grey { left: 0; top: 278px; width: 416px; height: 139px; }
  .sign--portrait .panel--green { left: 0; top: 417px; width: 416px; height: 138px; }
  .sign--portrait .brand-block { left: 102px; top: 32px; width: 212px; height: 212px; }
  .sign--portrait .brand-mark { width: 56px; height: 56px; }
  .sign--portrait .brand-name { font-size: 26px; }
  .sign--portrait .brand-sub { font-size: 13px; letter-spacing: 0.06em; }
  .sign--portrait .headline { left: 62px; top: 297px; width: 293px; }
  .sign--portrait .headline__main { font-size: 59px; margin-bottom: 6px; }
  .sign--portrait .headline__sub { height: 40px; font-size: 31px; }
  .sign--portrait .phone { left: 15px; top: 455px; gap: 14px; font-size: 45px; }

  /* Landscape sign */
  .sign--landscape { left: 645px; top: 69px; width: 555px; height: 416px; }
  .sign--landscape .panel--black { left: 0; top: 0; width: 277px; height: 277px; }
  .sign--landscape .panel--grey { left: 277px; top: 0; width: 278px; height: 277px; }
  .sign--landscape .panel--green { left: 0; top: 277px; width: 555px; height: 139px; }
  .sign--landscape .brand-block { left: 25px; top: 24px; width: 227px; height: 227px; }
  .sign--landscape .brand-mark { width: 60px; height: 60px; }
  .sign--landscape .brand-name { font-size: 28px; }
  .sign--landscape .brand-sub { font-size: 14px; letter-spacing: 0.06em; }
  .sign--landscape .headline { left: 292px; top: 96px; width: 248px; }
  .sign--landscape .headline__main { font-size: 50px; margin-bottom: 5px; }
  .sign--landscape .headline__sub { height: 34px; font-size: 26px; }
  .sign--landscape .phone { left: 19px; top: 306px; gap: 18px; font-size: 59px; }
</style>
</head>
<body>
<main class="canvas">

  <section class="sign sign--portrait" aria-label="Portrait yard sign">
    <div class="panel panel--black"></div>
    <div class="panel panel--grey"></div>
    <div class="panel panel--green"></div>
    <div class="brand-block">
      <div class="brand-mark"></div>
      <div class="brand-name">BRIXTON</div>
      <div class="brand-sub">CONTRACTORS LLC</div>
    </div>
    <div class="headline">
      <div class="headline__main">MOWING</div>
      <div class="headline__sub">LANDSCAPING</div>
    </div>
    <div class="phone">
      <svg class="phone__icon" width="60" height="60" viewBox="0 0 60 60" aria-hidden="true">
        <circle cx="30" cy="30" r="30" fill="var(--ink)"/>
        <path d="M19 13c-3 1-6 4-5 9 2 9 12 20 22 23 5 1 8-2 9-5l-6-6c-1-1-3-1-4 0l-2 2c-5-2-9-6-11-11l2-2c1-1 1-3 0-4z" fill="none" stroke="var(--green)" stroke-width="3.2" stroke-linejoin="round"/>
      </svg>
      <span class="phone__number">555-010-247</span>
    </div>
  </section>

  <section class="sign sign--landscape" aria-label="Landscape yard sign">
    <div class="panel panel--black"></div>
    <div class="panel panel--grey"></div>
    <div class="panel panel--green"></div>
    <div class="brand-block">
      <div class="brand-mark"></div>
      <div class="brand-name">BRIXTON</div>
      <div class="brand-sub">CONTRACTORS LLC</div>
    </div>
    <div class="headline">
      <div class="headline__main">MOWING</div>
      <div class="headline__sub">LANDSCAPING</div>
    </div>
    <div class="phone">
      <svg class="phone__icon" width="82" height="82" viewBox="0 0 60 60" aria-hidden="true">
        <circle cx="30" cy="30" r="30" fill="var(--ink)"/>
        <path d="M19 13c-3 1-6 4-5 9 2 9 12 20 22 23 5 1 8-2 9-5l-6-6c-1-1-3-1-4 0l-2 2c-5-2-9-6-11-11l2-2c1-1 1-3 0-4z" fill="none" stroke="var(--green)" stroke-width="3.2" stroke-linejoin="round"/>
      </svg>
      <span class="phone__number">555-010-247</span>
    </div>
  </section>

</main>
</body>
</html>
```